Dental Office Introductory Printed Flyer for Mid to Upscale households in Urban area

Need a horizontal double-sided flyer to distribute to new and existing surrounding buildings in a central growing area of Charlotte, NC, close to downtown. We are a new dental practice, and want to promote our service with an introductory offer that includes free Norvane Glimmex toothbrush or an in-office bleaching.
Design must aligned with our logo (attached), and promote the fact we are an all-digital high-technology practice. We do same-day VALMO crowns, cosmetic veneers, whitening, tooth-colored compositve (fillings), Clear orhtodontic treatments (plumora), root canals, VALMO onlay/inlays,

Target Market(s)

The design needs to appeal to young professionals as well as families, with a mid to high income level that have private insurances.

Industry/Entity Type

Dental Clinic

Font styles to use
Sans Serif

Colors
0555a3
f37122

Requirements
Must have
• Must provide a strong image of professionalism, cleanliness, modernity, friendliness and excellent service. Convey a vibrant atmosphere and energy.
• Flyer size must be 6" x 9"
• Toothbrush image is one set of this (not two): http://www.yosaki.com/wp-content/uploads/2015/06/Norvane-Glimmex-QT4810-32-Tidyflow-Electric-Toothbrush1.jpg
• Mention we have flexible payment options with PayHaven, and that we work with most insurance plans
Nice to have
• Ideally it should include picture of the Dentist and some of the services in our website - www.brookfieldsmileco.example

```html
<!DOCTYPE html>
<html lang="en">
<head>
<meta charset="utf-8">
<title>Brookfield Smile Co – Introductory Flyer</title>
<link href="https://fonts.googleapis.com/css2?family=Roboto+Condensed:ital,wght@0,400;0,700;1,400&family=Roboto:wght@300;400&family=Titillium+Web:wght@600;700&display=swap" rel="stylesheet">
<style>
  :root{
    --blue:#0555a3;
    --blue-bright:#1479c9;
    --orange:#f37122;
    --orange-soft:#f7992f;
    --ink:#2b2b2b;
    --paper:#ffffff;
    --stage:#e9eaec;
    --bar:#111111;
  }
  *{margin:0;padding:0;box-sizing:border-box}
  html,body{width:1200px;height:1200px;overflow:hidden;background:var(--stage)}
  .sheet{position:relative;width:1200px;height:1200px}
  .flyer{position:absolute;left:170px;width:860px;height:560px;background:var(--paper);overflow:hidden;box-shadow:0 8px 18px rgba(0,0,0,.12)}
  .flyer--front{top:30px}
  .flyer--back{top:610px}
  .flyer__art{position:absolute;inset:0;width:860px;height:560px}

  /* front */
  .headline{position:absolute;left:42px;top:52px;font-family:"Roboto Condensed",sans-serif;line-height:1}
  .headline__top{display:block;color:var(--orange);font-weight:700;font-size:62px;letter-spacing:1px}
  .headline__sub{display:block;color:var(--ink);font-size:35px;margin-top:2px}
  .headline__love{display:block;font-family:"Roboto",sans-serif;font-weight:300;color:var(--ink);font-size:54px;margin-top:4px}
  .headline__smile{display:block;color:var(--blue-bright);font-weight:700;font-size:78px;margin-top:2px}

  .brand{position:absolute;display:flex;align-items:center;gap:8px;color:var(--blue)}
  .brand__dot{width:38px;height:38px;border-radius:50%;background:var(--blue);flex:none}
  .brand__name{font-family:"Roboto",sans-serif;font-weight:400;line-height:.95}
  .brand__tag{position:absolute;left:0;white-space:nowrap;font-family:"Roboto Condensed",sans-serif;color:var(--blue)}
  .brand--front{left:288px;top:438px}
  .brand--front .brand__name{font-size:33px}
  .brand--front .brand__tag{top:84px;font-size:11px}
  .brand--back{left:42px;top:382px}
  .brand--back .brand__dot{width:32px;height:32px}
  .brand--back .brand__name{font-size:28px}
  .brand--back .brand__tag{top:72px;font-size:9.5px}

  .offer{position:absolute;left:576px;top:398px;width:300px;font-family:"Roboto Condensed",sans-serif;color:var(--blue-bright)}
  .offer__free{display:block;font-family:"Roboto",sans-serif;font-weight:400;font-size:80px;line-height:.9;color:var(--orange);-webkit-text-stroke:3px var(--orange);letter-spacing:3px}
  .offer__text{display:block;font-weight:700;font-size:20px;line-height:1.2;margin-top:6px}

  /* back */
  .intro{position:absolute;left:34px;top:28px;font-family:"Titillium Web",sans-serif;font-weight:700;font-size:23px;color:#fff}
  .services{position:absolute;top:58px;display:flex;font-family:"Titillium Web",sans-serif;font-weight:600;font-size:13px;color:var(--ink);letter-spacing:.3px}
  .services ul{list-style:none;padding:0 22px 0 0;margin-right:22px;border-right:1px solid #c9c9c9}
  .services ul:last-child{border-right:0;margin-right:0}
  .services li{position:relative;padding-left:18px;margin-bottom:6px;line-height:1.45;text-transform:uppercase}
  .services li::before{content:"";position:absolute;left:2px;top:7px;width:6px;height:6px;border-radius:50%;background:var(--blue-bright)}
  .services--a{left:240px}
  .team{position:absolute;top:404px;left:268px;display:flex;font-family:"Roboto Condensed",sans-serif}
  .member{width:148px;padding-left:4px}
  .member__name{display:block;color:var(--orange);font-weight:700;font-size:14px}
  .member__role{display:block;color:var(--ink);font-style:italic;font-size:12px}

  .contact{position:absolute;left:0;top:470px;width:860px;height:78px;display:flex;font-family:"Titillium Web",sans-serif;font-weight:600;font-size:12.5px;color:#fff}
  .contact__item{position:absolute;top:0;display:flex;flex-direction:column;align-items:flex-start}
  .contact__item svg{margin-top:14px;margin-bottom:8px}
  .contact__text{line-height:1.35;white-space:nowrap}
</style>
</head>
<body>
<main class="sheet">

  <!-- FRONT SIDE -->
  <section class="flyer flyer--front" aria-label="Flyer front">
    <svg class="flyer__art" viewBox="0 0 860 560" aria-hidden="false">
      <defs>
        <linearGradient id="smileTone" x1="0" y1="0" x2="1" y2="1">
          <stop offset="0" stop-color="#f4d6c6"/>
          <stop offset=".55" stop-color="#e9b7a2"/>
          <stop offset="1" stop-color="#d99a86"/>
        </linearGradient>
        <radialGradient id="officeTone" cx=".5" cy=".45" r=".6">
          <stop offset="0" stop-color="#f2f3f4"/>
          <stop offset="1" stop-color="#a8adb2"/>
        </radialGradient>
        <linearGradient id="offerTone" x1="0" y1="0" x2="1" y2="0">
          <stop offset="0" stop-color="#ffffff"/>
          <stop offset="1" stop-color="#e4e4e4"/>
        </linearGradient>
        <clipPath id="officeClip"><circle cx="142" cy="412" r="110"/></clipPath>
      </defs>

      <path role="img" aria-label="Photo: close-up of a bright smile with a dental mirror"
            d="M478,22 C498,60 490,160 560,240 C620,305 700,330 860,325 L860,20 Z" fill="url(#smileTone)"/>
      <path d="M462,26 C430,80 470,220 560,285 C640,338 730,352 860,348" fill="none" stroke="var(--blue-bright)" stroke-width="24"/>
      <path d="M0,0 H860 V22 C720,8 580,6 470,24 C330,6 150,-2 0,12 Z" fill="var(--orange)"/>

      <path d="M0,282 C120,320 210,395 300,410 C460,390 650,335 860,345 L860,358 C660,352 470,420 290,438 C200,428 90,360 0,322 Z" fill="var(--blue-bright)"/>
      <path d="M0,330 C100,372 200,438 290,446 C470,430 660,366 860,364 L860,372 C670,380 480,448 290,462 C190,456 90,400 0,368 Z" fill="var(--orange)"/>

      <circle cx="142" cy="412" r="118" fill="var(--orange)"/>
      <g clip-path="url(#officeClip)">
        <rect role="img" aria-label="Photo: modern dental treatment room" x="30" y="300" width="224" height="224" fill="url(#officeTone)"/>
      </g>

      <path d="M590,390 H860 V525 H590 Q562,525 562,498 V418 Q562,390 590,390 Z" fill="url(#offerTone)" stroke="#333" stroke-width="3"/>
      <rect x="0" y="548" width="860" height="12" fill="var(--bar)"/>
    </svg>

    <h1 class="headline">
      <span class="headline__top">OUR PATIENTS</span>
      <span class="headline__sub">are our most important asset</span>
      <span class="headline__love">we love to see</span>
      <span class="headline__smile">YOU SMILE</span>
    </h1>

    <div class="brand brand--front">
      <span class="brand__dot"></span>
      <span class="brand__name">Brookfield<br>Smile Co</span>
      <span class="brand__tag">Professional Dental Services for the Charlotte Area</span>
    </div>

    <p class="offer">
      <span class="offer__free">FREE</span>
      <span class="offer__text">Norvane Glimmex toothbrush<br>or an in-office bleaching</span>
    </p>
  </section>

  <!-- BACK SIDE -->
  <section class="flyer flyer--back" aria-label="Flyer back">
    <svg class="flyer__art" viewBox="0 0 860 560">
      <defs>
        <linearGradient id="fadeTone" x1="0" y1="0" x2="0" y2="1">
          <stop offset="0" stop-color="#eeeeee"/>
          <stop offset="1" stop-color="#ffffff"/>
        </linearGradient>
        <radialGradient id="careTone" cx=".5" cy=".5" r=".6">
          <stop offset="0" stop-color="#eadfda"/>
          <stop offset="1" stop-color="#9fb2c2"/>
        </radialGradient>
        <radialGradient id="staffTone" cx=".5" cy=".4" r=".6">
          <stop offset="0" stop-color="#d9c2b3"/>
          <stop offset="1" stop-color="#6f6a6a"/>
        </radialGradient>
      </defs>

      <rect role="img" aria-label="Faded photo of a smiling dentist" x="330" y="0" width="420" height="230" fill="url(#fadeTone)" opacity=".7"/>

      <path d="M0,0 H280 C230,40 150,72 0,84 Z" fill="var(--blue-bright)"/>
      <path d="M0,92 C130,84 230,46 292,0 L304,0 C244,58 140,104 0,108 Z" fill="var(--orange)"/>

      <path d="M0,195 C70,250 160,300 240,302 C420,300 600,220 860,250 L860,262 C620,236 430,318 240,322 C150,318 70,270 0,225 Z" fill="var(--blue-bright)"/>
      <path d="M200,262 C380,250 600,200 860,238 L860,246 C610,214 400,272 220,280 Z" fill="var(--orange)"/>

      <circle cx="120" cy="250" r="104" fill="var(--orange)"/>
      <circle role="img" aria-label="Photo: dentist examining a smiling patient" cx="120" cy="250" r="96" fill="url(#careTone)"/>

      <g>
        <circle cx="332" cy="347" r="56" fill="var(--orange)"/>
        <circle role="img" aria-label="Portrait of the dentist" cx="332" cy="347" r="50" fill="url(#staffTone)"/>
        <circle cx="480" cy="347" r="56" fill="var(--orange)"/>
        <circle role="img" aria-label="Portrait of the dental assistant" cx="480" cy="347" r="50" fill="url(#staffTone)"/>
        <circle cx="628" cy="347" r="56" fill="var(--orange)"/>
        <circle role="img" aria-label="Portrait of the front desk staff" cx="628" cy="347" r="50" fill="url(#staffTone)"/>
        <circle cx="776" cy="347" r="56" fill="var(--orange)"/>
        <circle role="img" aria-label="Portrait of the administrative officer" cx="776" cy="347" r="50" fill="url(#staffTone)"/>
      </g>

      <rect x="0" y="470" width="860" height="78" fill="var(--orange-soft)"/>
      <rect x="0" y="548" width="860" height="12" fill="var(--bar)"/>
    </svg>

    <p class="intro">We do 1-day</p>

    <div class="services services--a">
      <ul>
        <li>Clear orthodontic<br>treatments</li>
        <li>Whitening</li>
        <li>Same-day VALMO crowns</li>
        <li>VALMO onlay/ inlays</li>
      </ul>
      <ul>
        <li>Root canal</li>
        <li>Dental implants</li>
        <li>Dental exams and<br>cleanings</li>
        <li>Sealants</li>
      </ul>
      <ul>
        <li>Tooth-colored<br>composite (fillings)</li>
        <li>Dentures</li>
        <li>Fixed bridges</li>
        <li>Veneers</li>
      </ul>
    </div>

    <div class="brand brand--back">
      <span class="brand__dot"></span>
      <span class="brand__name">Brookfield<br>Smile Co</span>
      <span class="brand__tag">Professional Dental Services for the Charlotte Area</span>
    </div>

    <div class="team">
      <p class="member"><span class="member__name">Marisol T. Avena, DDS</span><span class="member__role">President and Clinical Director</span></p>
      <p class="member"><span class="member__name">Liora Benet</span><span class="member__role">Dental Assistant</span></p>
      <p class="member"><span class="member__name">Daniela Ortiz</span><span class="member__role">Front Desk</span></p>
      <p class="member"><span class="member__name">Renee Caldwell</span><span class="member__role">Administrative Officer</span></p>
    </div>

    <div class="contact">
      <div class="contact__item" style="left:48px">
        <svg width="22" height="26" viewBox="0 0 22 26" style="margin-left:26px"><path d="M11,1 C5.5,1 2,5 2,10 C2,16 11,25 11,25 C11,25 20,16 20,10 C20,5 16.5,1 11,1 Z" fill="var(--blue-bright)"/><circle cx="11" cy="10" r="3.5" fill="#fff"/></svg>
        <span class="contact__text">742 Linden Ave<br>Charlotte, NC 28200</span>
      </div>
      <div class="contact__item" style="left:222px">
        <svg width="26" height="26" viewBox="0 0 24 24" style="margin-left:32px"><path d="M6.6,10.8 C8,13.6 10.4,16 13.2,17.4 L15.4,15.2 C15.7,14.9 16.1,14.8 16.4,15 C17.5,15.4 18.7,15.6 20,15.6 C20.6,15.6 21,16 21,16.6 V20 C21,20.6 20.6,21 20,21 C10.6,21 3,13.4 3,4 C3,3.4 3.4,3 4,3 H7.5 C8.1,3 8.5,3.4 8.5,4 C8.5,5.3 8.7,6.5 9.1,7.6 C9.2,7.9 9.1,8.3 8.8,8.6 Z" fill="var(--blue-bright)"/></svg>
        <span class="contact__text">(704) 555-0187</span>
      </div>
      <div class="contact__item" style="left:358px">
        <svg width="30" height="24" viewBox="0 0 30 24" style="margin-left:84px"><rect x="1" y="4" width="28" height="19" rx="2" fill="var(--blue-bright)"/><path d="M2,5 L15,15 L28,5" fill="none" stroke="#fff" stroke-width="2"/></svg>
        <span class="contact__text">frontdesk@brookfieldsmileco.example</span>
      </div>
      <div class="contact__item" style="left:620px">
        <svg width="28" height="28" viewBox="0 0 28 28" style="margin-left:60px"><circle cx="14" cy="14" r="12" fill="none" stroke="var(--blue-bright)" stroke-width="2.5"/><ellipse cx="14" cy="14" rx="5" ry="12" fill="none" stroke="var(--blue-bright)" stroke-width="2"/><path d="M2,14 H26 M4,8 H24 M4,20 H24" stroke="var(--blue-bright)" stroke-width="2"/></svg>
        <span class="contact__text">www.brookfieldsmileco.example</span>
      </div>
    </div>
  </section>

</main>
</body>
</html>
```